Visitenkarten-Design für Eventcatering & Gemeinschaftsverpflegung
Zielgruppe
Wir sind ein kreatives und aufstrebendes Unternehmen.
Seit jahren sind wir im Eventcatering und der Gemeinschaftsverpflegung tätig.
Als Marktführer kochen wir super leckeres Mittagessen für Grundschulen und Kindertagesstätten in Berlin und Brandenburg und bewirtschaften mehrere Betriebsrestaurants.
Wir sind sehr krativ und bleiben nie stehen, so bereichern wir die Gastronomie in allen
Bereichen mit immer neuen innovativen Ideen und der Leidenschaft zum gesunden und leckeren Essen.
We are a creative and ambitious company.
We have been active in event catering and community catering for years.
As the market leader, we cook delicious lunches for elementary schools and day-care centers in Berlin and Brandenburg and we run several company restaurants.
We are very creative and never stand still, this is how we enrich the gastronomy in all of them
areas with new, innovative ideas and a passion for healthy and delicious food.
Aufgabenstellung
Wir möchten gern die Rottöne aus unserem Logo wiederfinden.
Unser Logo darf im Vordergrund stehen.
We would like to find the red tones from our logo again.
Our logo can be in the foreground.

```html
<!DOCTYPE html>
<html lang="en">
<head>
<meta charset="utf-8">
<title>Velora Catering – Business Cards</title>
<link href="https://fonts.googleapis.com/css2?family=Open+Sans:wght@400;600;700&display=swap" rel="stylesheet">
<style>
  :root {
    --page-bg: #e9e9ea;
    --card-white: #ffffff;
    --brand-red: #e8262b;
    --ink: #1c1c1c;
    --ink-soft: #3a3a3a;
    --white: #ffffff;
  }
  * { margin: 0; padding: 0; box-sizing: border-box; }
  html, body { width: 1200px; height: 977px; overflow: hidden; }
  body {
    background: var(--page-bg);
    font-family: "Open Sans", Arial, sans-serif;
    color: var(--ink);
    position: relative;
  }
  .card {
    position: absolute;
    top: 320px;
    width: 520px;
    height: 336px;
    border-radius: 22px;
    box-shadow: 0 6px 18px rgba(0,0,0,0.12);
  }
  .card--front { left: 50px; background: var(--card-white); }
  .card--back  { left: 630px; background: var(--brand-red); }

  .brand {
    position: absolute;
    display: flex;
    align-items: center;
    gap: 10px;
    font-weight: 700;
  }
  .brand__mark { width: 30px; height: 30px; background: var(--brand-red); }
  .card--front .brand { left: 38px; top: 38px; font-size: 34px; color: var(--ink); }
  .card--back .brand {
    left: 50%; top: 50%; transform: translate(-50%, -50%);
    font-size: 46px; color: var(--white);
  }
  .card--back .brand__mark { width: 40px; height: 40px; background: var(--white); }

  .person { position: absolute; left: 300px; top: 135px; }
  .person__name { font-size: 21px; font-weight: 700; line-height: 1.2; }
  .person__role { font-size: 13px; color: var(--ink-soft); }

  .contact {
    position: absolute;
    top: 220px;
    font-size: 14px;
    line-height: 1.45;
    color: var(--ink-soft);
    list-style: none;
  }
  .contact--reach { left: 38px; }
  .contact--place { left: 300px; }
</style>
</head>
<body>
  <section class="card card--front" aria-label="Business card front">
    <div class="brand"><span class="brand__mark"></span><span class="brand__name">Velora Catering</span></div>
    <div class="person">
      <p class="person__name">Lina Marsk</p>
      <p class="person__role">Chief Financial Officer</p>
    </div>
    <ul class="contact contact--reach">
      <li>+46 8 123 45 67</li>
      <li>+46 70 123 45 67</li>
      <li>lina@velorakok.se</li>
    </ul>
    <ul class="contact contact--place">
      <li>www.velorakok.se</li>
      <li>Ekgatan 7, SE-123 45</li>
      <li>NORRVIK, Sweden</li>
    </ul>
  </section>

  <section class="card card--back" aria-label="Business card back">
    <div class="brand"><span class="brand__mark"></span><span class="brand__name">Velora Catering</span></div>
  </section>
</body>
</html>
```